business card design for luxurious real estate brand

using the attached logo, i am looking for a 2-sided business card design. the back should be the gold logo on black background. the front needs to include: gold logo, name, phone, email, and website

Industry/Entity Type

real estate

Contact Information for Business Card

logo, name, email, phone, website

Font styles to use
Sans Serif

```html
<!DOCTYPE html>
<html lang="en">
<head>
<meta charset="utf-8">
<title>Casa Ridgeview — Business Card</title>
<link href="https://fonts.googleapis.com/css2?family=Lato:wght@400;700;900&display=swap" rel="stylesheet">
<style>
  :root {
    --canvas: #151616;
    --card: #1d1d1d;
    --gold: #d6ae52;
    --gold-text: #c99a2e;
    --yellow: #e9b80c;
  }
  * { margin: 0; padding: 0; box-sizing: border-box; }
  html, body {
    width: 1200px; height: 975px; overflow: hidden;
    background: var(--canvas);
    font-family: "Lato", sans-serif;
  }
  .card {
    position: absolute;
    width: 560px; height: 320px;
    background: var(--card);
    overflow: hidden;
  }
  .card--back { left: 560px; top: 110px; }
  .card--front { left: 90px; top: 540px; }
  .card__accent { position: absolute; inset: 0; width: 100%; height: 100%; }

  .brand {
    position: absolute;
    display: flex; align-items: center; gap: 10px;
    color: var(--gold);
    font-weight: 700;
    text-transform: uppercase;
    white-space: nowrap;
  }
  .brand__dot {
    width: 12px; height: 12px; border-radius: 50%;
    background: var(--gold);
    flex: none;
  }
  .card--back .brand {
    left: 0; right: 0; top: 168px; justify-content: center;
    font-size: 30px; letter-spacing: 9px;
  }
  .card--front .brand {
    left: 28px; top: 124px;
    font-size: 16px; letter-spacing: 3px;
  }

  .divider {
    position: absolute; left: 300px; top: 60px;
    width: 1px; height: 152px; background: var(--gold-text);
  }
  .contact {
    position: absolute; left: 322px; top: 64px;
    color: var(--gold-text);
  }
  .contact__name { font-size: 22px; font-weight: 900; letter-spacing: 0.5px; text-transform: uppercase; }
  .contact__role { font-size: 14px; margin-top: 2px; margin-bottom: 12px; }
  .contact__line {
    display: flex; align-items: center; gap: 8px;
    font-size: 14px; line-height: 23px;
    white-space: nowrap;
  }
  .contact__icon { width: 12px; height: 12px; fill: var(--gold-text); flex: none; }
</style>
</head>
<body>

  <section class="card card--back">
    <svg class="card__accent" viewBox="0 0 560 320" preserveAspectRatio="none" aria-hidden="true">
      <polygon points="0,0 300,0 0,170" fill="var(--yellow)"/>
    </svg>
    <div class="brand"><span class="brand__dot"></span>Casa Ridgeview</div>
  </section>

  <section class="card card--front">
    <svg class="card__accent" viewBox="0 0 560 320" preserveAspectRatio="none" aria-hidden="true">
      <polygon points="560,220 560,320 380,320" fill="var(--yellow)"/>
    </svg>
    <div class="brand"><span class="brand__dot"></span>Casa Ridgeview</div>
    <div class="divider"></div>
    <div class="contact">
      <p class="contact__name">Daniel Hart</p>
      <p class="contact__role">CEO &amp; Founder</p>
      <p class="contact__line">
        <svg class="contact__icon" viewBox="0 0 24 24"><path d="M6.6 10.8a15 15 0 0 0 6.6 6.6l2.2-2.2a1 1 0 0 1 1-.25 11.4 11.4 0 0 0 3.6.57 1 1 0 0 1 1 1V20a1 1 0 0 1-1 1A17 17 0 0 1 3 4a1 1 0 0 1 1-1h3.5a1 1 0 0 1 1 1c0 1.250.2 2.45.57 3.57a1 1 0 0 1-.25 1z"/></svg>
        (555) 018-2744
      </p>
      <p class="contact__line">
        <svg class="contact__icon" viewBox="0 0 24 24"><path d="M2 5h20v14H2z M2 5l10 8 10-8" fill="none" stroke="var(--gold-text)" stroke-width="2.4"/></svg>
        hello@casaridgeview.com
      </p>
      <p class="contact__line">
        <svg class="contact__icon" viewBox="0 0 24 24"><circle cx="12" cy="12" r="10" fill="none" stroke="var(--gold-text)" stroke-width="2.4"/><path d="M2 12h20M12 2c3 3 3 17 0 20M12 2c-3 3-3 17 0 20" fill="none" stroke="var(--gold-text)" stroke-width="2"/></svg>
        casaridgeview.com
      </p>
    </div>
  </section>

</body>
</html>
```